Postcard Design

Postcard for the following:

Front of postcard:
A new little beauty and health haven has opened up just around the corner at 42 Marston Lane, Fernwood Rise.
Just like you, Mabel’s Lantern is special, offering treatments and services tailor made to your specific needs. Mabel has over 24 years of industry experience and offers a unique approach to helping you feel healthful, nourished and happy. Her treatments are brilliantly effective and include remedial massage therapies and reflexology, gorgeous rejuvenating facials and much much more…………..come and experience this unique and 100% organic little piece of heaven.
You deserve to feel great so we work from the inside out by offering nutritional health advice and formulations developed especially for you. We wholly nourish the individual in the wise woman tradition of healing and happiness.
As a special welcome gift I would like to offer you $15 off any service
By appointment 027 5162930 I look forward to seeing you soon

Back of postcard:
The hearth has been the centre of human life for at least 400,000 years. it is the place where people meet to cook, eat, talk together and heal. The ' hearth' was the heart of the home It was the centre of activity, where everyone gathered to keep warm, laugh, listen to the stories of old and heal. It was the place of physical and emotional nourishment. The hearth is a symbol for the hospitality and living spirit of the home.

Industry/Entity Type

Hospitality

Requirements
Nice to have
• A logo for the business would be really good.

```html
<!DOCTYPE html>
<html lang="en">
<head>
<meta charset="utf-8">
<title>Mabel’s Lantern Postcard</title>
<link href="https://fonts.googleapis.com/css2?family=Questrial&display=swap" rel="stylesheet">
<style>
  :root {
    --stage: #d6d6d6;
    --red-a: #ea5a4e;
    --red-b: #e0245e;
    --brand-red: #d2283c;
    --blush: #fbe4e0;
    --navy: #25223f;
    --white: #ffffff;
    --ring: #f6a3a8;
  }
  * { box-sizing: border-box; margin: 0; padding: 0; }
  html, body {
    width: 1058px; height: 1200px; overflow: hidden;
    background: var(--stage);
    font-family: "Questrial", "Century Gothic", sans-serif;
  }
  .postcard {
    position: absolute; left: 109px; width: 840px; height: 540px;
    overflow: hidden; box-shadow: 0 8px 22px rgba(0,0,0,.22);
  }
  .postcard--front { top: 40px; background: linear-gradient(135deg, var(--red-a), var(--red-b)); }
  .postcard--back { top: 620px; background: var(--white); }

  .photo { position: absolute; left: 0; top: 0; width: 840px; height: 540px; }

  .brand { position: absolute; display: flex; align-items: center; gap: 10px; font-size: 21px; }
  .brand__dot { width: 26px; height: 26px; border-radius: 50%; }
  .postcard--front .brand { left: 40px; top: 30px; color: var(--white); }
  .postcard--front .brand__dot { background: var(--white); }
  .postcard--back .brand { left: 46px; top: 40px; color: var(--brand-red); }
  .postcard--back .brand__dot { background: var(--brand-red); }

  .front-copy {
    position: absolute; left: 40px; top: 78px; width: 420px;
    color: var(--white); font-size: 13.2px; line-height: 1.3; text-align: justify;
  }
  .front-copy .lead { font-size: 15px; font-weight: 700; letter-spacing: .2px; margin-bottom: 10px; }
  .front-copy p + p { margin-top: 10px; }

  .offer-band {
    position: absolute; left: 0; bottom: 48px; width: 540px; height: 52px;
    background: var(--blush); color: var(--navy);
    font-size: 15px; line-height: 1.2; padding: 7px 0 0 44px;
  }
  .offer-band .amount { color: var(--brand-red); font-size: 16px; }
  .contact-band {
    position: absolute; left: 0; bottom: 0; width: 100%; height: 48px;
    background: var(--navy); color: var(--white);
    font-size: 19px; letter-spacing: .5px;
    display: flex; align-items: center; padding-left: 100px;
  }
  .contact-band__tail {
    position: absolute; right: 0; bottom: 48px; width: 300px; height: 52px;
    background: var(--navy);
  }

  .section-tag {
    position: absolute; left: 40px; top: 98px; width: 210px; height: 28px;
    background: linear-gradient(90deg, var(--brand-red) 55%, rgba(210,40,60,.35));
    color: var(--white); font-size: 17px; padding: 3px 0 0 10px;
  }
  .back-copy {
    position: absolute; left: 46px; top: 136px; width: 320px;
    color: var(--brand-red); font-size: 15.5px; line-height: 1.33; text-align: justify;
  }
</style>
</head>
<body>

<section class="postcard postcard--front">
  <svg class="photo" viewBox="0 0 840 540" role="img" aria-label="Photograph of a woman relaxing under a white towel at a spa, with pink blossoms behind her">
    <defs>
      <radialGradient id="photoTone" cx="0.55" cy="0.45" r="0.6">
        <stop offset="0" stop-color="#f6efef"/>
        <stop offset="0.55" stop-color="#ecd6d3"/>
        <stop offset="1" stop-color="#d9b3ae"/>
      </radialGradient>
    </defs>
    <circle cx="660" cy="205" r="292" fill="var(--ring)" opacity="0.45"/>
    <circle cx="660" cy="205" r="272" fill="url(#photoTone)"/>
  </svg>

  <div class="brand"><span class="brand__dot"></span><span>Mabel’s Lantern</span></div>

  <div class="front-copy">
    <p class="lead">A new little beauty and health haven has opened up just around the corner at 42 Marston Lane, Fernwood Rise.</p>
    <p>Just like you, Mabel’s Lantern is special, offering treatments and services tailor made to your specific needs. Mabel has over 24 years of industry experience and offers a unique approach to helping you feel healthful, nourished and happy. Her treatments are brilliantly effective and include remedial massage therapies and reflexology, gorgeous rejuvenating facials and much much more…………..come and experience this unique and 100% organic little piece of heaven.</p>
    <p>You deserve to feel great so we work from the inside out by offering nutritional health advice and formulations developed especially for you. We wholly nourish the individual in the wise woman tradition of healing and happiness.</p>
  </div>

  <div class="contact-band__tail"></div>
  <div class="offer-band">
    As a special welcome gift I would like to offer you<br>
    <span class="amount">$15</span> off any service
  </div>
  <div class="contact-band">By appointment 027 5162930 I look forward to seeing you soon</div>
</section>

<section class="postcard postcard--back">
  <div class="brand"><span class="brand__dot"></span><span>Mabel’s Lantern</span></div>
  <div class="section-tag">What is a hearth . . .</div>
  <p class="back-copy">The hearth has been the centre of human life for at least 400,000 years. It is the place where people meet to cook, eat and talk together and heal. The ‘hearth’ was the heart of the home. It was the centre of activity, where everyone gathered to eat and cook, to sit and warm themselves, and listen to the stories of old. It was the place of physical and emotional nourishment. The hearth is a symbol for the hospitality and living spirit of the home.</p>
</section>

</body>
</html>
```